Harlow Finch Ltd. Recruitment Brochure

A 12pp A4 portrait brochure is required. It should have a contemporary and modern feel to it.

Please feel free to bring the flow chart to life with symbols that reflect the title of the stage in the flow chart.

Similarly the services that are offered should be brought to life.

See the attached brief for the detailed copy and brand colour details. I have also attached the logo and imagery to be used although we are open to additional / alternative imagery as long as it is royalty free and won't cost any additional money.

Target Market(s)

Small and medium sized businesses

Industry/Entity Type

Recruitment

Font styles to use
Serif
Sans Serif

Requirements
Must have
• See project brief.
Nice to have
• See project brief - bringing the flow chart and services aspects to life would be good.
Should not have
• See project brief.

```html
<!DOCTYPE html>
<html lang="en">
<head>
<meta charset="utf-8">
<title>Harlow Finch Ltd. – Brochure Spread, Pages 5–6</title>
<link href="https://fonts.googleapis.com/css2?family=Montserrat:wght@400;500;600;700&display=swap" rel="stylesheet">
<style>
  :root {
    --maroon: #7b1d3d;
    --maroon-deep: #6a1733;
    --ink: #2b2b2e;
    --body: #3a3a3c;
    --paper: #f6f6f6;
    --header-paper: #efeff0;
    --stage: #d6d4d2;
    --overlay: rgba(38, 40, 46, 0.86);
    --photo-light: #d9dde4;
    --photo-mid: #8f8a95;
    --photo-dark: #2f3445;
  }
  * { box-sizing: border-box; margin: 0; padding: 0; }
  html, body { width: 1200px; height: 900px; overflow: hidden; }
  body {
    background: var(--stage);
    font-family: "Montserrat", Arial, sans-serif;
    color: var(--body);
    position: relative;
  }
  .spread {
    position: absolute;
    left: 20px; top: 33px;
    width: 1160px; height: 834px;
    display: flex;
    box-shadow: 0 6px 24px rgba(0,0,0,0.25);
  }
  .page {
    position: relative;
    width: 580px; height: 834px;
    background: var(--paper);
    overflow: hidden;
  }
  .page-head {
    position: absolute; left: 0; top: 0; right: 0;
    height: 64px;
    border-bottom: 1.5px solid var(--maroon);
    background: var(--header-paper);
  }
  .page-number {
    position: absolute; top: 48px;
    font-size: 10px; font-weight: 600; color: var(--ink);
  }
  .page--left .page-number { left: 30px; }
  .page--right .page-number { right: 24px; }
  .brand-mark {
    position: absolute; top: 30px;
    display: flex; align-items: center; gap: 6px;
    font-size: 13px; font-weight: 700; color: var(--maroon);
    letter-spacing: 0.02em;
  }
  .brand-mark .dot {
    width: 12px; height: 12px; border-radius: 50%;
    background: var(--maroon);
  }
  .page--left .brand-mark { left: 52px; }
  .page--right .brand-mark { left: 60px; }
  .running-title {
    position: absolute; top: 44px;
    font-size: 9.5px; font-weight: 700; color: var(--maroon);
    letter-spacing: 0.03em;
  }
  .page--left .running-title { right: 50px; }
  .page--right .running-title { right: 46px; }

  .title-zone {
    position: absolute; left: 0; right: 0; top: 65px; height: 104px;
    background: var(--header-paper);
  }
  .spread-title {
    position: absolute; left: 45px; top: 40px;
    font-size: 22px; font-weight: 700; letter-spacing: 0.03em;
    color: var(--ink);
  }
  .spread-title .accent { color: var(--maroon); }

  .intro-band {
    position: absolute; left: 0; right: 0; top: 169px; height: 124px;
    background: var(--maroon);
    color: #fff;
    display: flex; gap: 38px;
    padding: 22px 28px 0 27px;
    font-size: 8.6px; line-height: 12px;
  }
  .intro-band p:first-child { width: 222px; }
  .intro-band p:last-child { width: 235px; }

  .columns {
    position: absolute; left: 27px; top: 322px;
    display: flex; gap: 38px;
  }
  .column { width: 230px; }
  .column:last-child { width: 235px; }
  .service-title {
    font-size: 11px; font-weight: 700; color: var(--maroon);
    margin-bottom: 12px;
  }
  .column p {
    font-size: 8.6px; line-height: 12px; color: var(--body);
    margin-bottom: 10px;
  }
  .column p + .service-title { margin-top: 4px; }

  .photo {
    position: absolute; left: 0; right: 0; top: 169px; height: 638px;
    background:
      radial-gradient(ellipse at 20% 15%, var(--photo-light) 0%, rgba(217,221,228,0) 55%),
      linear-gradient(115deg, #c8ccd6 0%, var(--photo-mid) 45%, var(--photo-dark) 100%);
  }
  .photo-caption {
    position: absolute; left: 0; right: 0; bottom: 0; height: 188px;
    background: var(--overlay);
    color: #f1f1f3;
    padding: 38px 40px 0 28px;
    font-size: 8.6px; line-height: 12px;
  }
  .photo-caption h2 {
    font-size: 11px; font-weight: 600; margin-bottom: 14px;
  }
  .photo-caption p { margin-bottom: 12px; }
</style>
</head>
<body>
  <main class="spread">
    <section class="page page--left">
      <header class="page-head">
        <span class="page-number">5</span>
        <span class="brand-mark"><span class="dot"></span>Harlow Finch</span>
        <span class="running-title">HARLOW FINCH</span>
      </header>
      <div class="title-zone">
        <h1 class="spread-title"><span class="accent">DELIVERING WORLD</span> CLASS SOLUTIONS</h1>
      </div>
      <div class="intro-band">
        <p>Whilst we can offer the full range of sales recruitment services, the very first step we take is getting an in-depth understanding of you, our client, including not just the role you are recruiting for but your company culture as well.</p>
        <p>Once we have got a really good understanding of your requirements, we are experts at identifying and delivering to those needs. We will present the best options to help ensure we choose the right solution to find the ideal sales person who is a perfect match for both the role and your company.</p>
      </div>
      <div class="columns">
        <div class="column">
          <h2 class="service-title">Our Headhunting Service</h2>
          <p>How can you recruit the very best senior sales talent out there if they are being kept happy by their existing employer and are not actively looking for a role? They will not respond to adverts and they will not have registered with any recruitment agencies but they will move if the right opportunity is presented to them. The answer is using an expert headhunting service.</p>
          <p>We research the whole market to find all of the relevant and top performing sales people (within both your industry and other relevant markets), who would be suitable for a role and approach them to present the benefits of working for your organisation.</p>
          <p>This service provides complete transparency and accountability for finding the best available person for your company, so you can have complete peace of mind that wherever the perfect candidate is, we will find them!</p>
          <h2 class="service-title">Abbreviated Search Service</h2>
          <p>For roles where the salary may not justify the costs of a full headhunt, we can also undertake an abbreviated search project to recruit senior sales people. This unique sales recruitment service involves undertaking a smaller scale search process at a lower cost and in quicker time but you also get the benefits of our headhunting expertise.</p>
        </div>
        <div class="column">
          <h2 class="service-title">Success-only recruitment</h2>
          <p>We can also undertake success-only sales recruitment services for you whereby we can advertise roles and deal with all of the responses. Of course we will also have the advantage of a high quality extensive contact network that we can tap into in order to potentially find a great candidate for your organisation.</p>
          <p>Of course whenever we come across a great candidate who we think would be a great fit for your organisation, we will always approach you with them on a success-only basis.</p>
          <h2 class="service-title">Psychometric and job profiling</h2>
          <p>Because we know how critically important it is for any individual joining your company to be the right cultural fit, we always complement our services with the use of psychometric and job profiling. We use both these services as an integral aspect of our headhunting process and the profiles help to make sure the candidate is perfect for both the role and the company.</p>
          <p>Psychometric profiling assesses a candidate's personality and characteristics to identify their strengths as well as potential development areas.</p>
          <p>Job profiling focusses on identifying the right personality required as well as the skills and experience of the ideal candidate for a role. This allows you to compare the psychometric profile of a candidate to the profile required for the job and therefore how closely matched the candidate will be.</p>
        </div>
      </div>
    </section>

    <section class="page page--right">
      <header class="page-head">
        <span class="brand-mark"><span class="dot"></span>Harlow Finch</span>
        <span class="running-title">HARLOW FINCH</span>
        <span class="page-number">6</span>
      </header>
      <div class="title-zone"></div>
      <div class="photo" role="img" aria-label="Photograph of two smiling businessmen in suits reviewing work together at a desk in a bright office">
        <div class="photo-caption">
          <h2>Competency interviews</h2>
          <p>We are experts in competency interviews and firmly believe they provide real value in determining the suitability of a candidate for a role as they require the candidate to provide specific examples against a range of competencies. We can even help you identify the right competencies for a role if you wish.</p>
          <p>As part of our sales headhunting service, on projects where we undertake competency interviews alongside you, we offer an extension from our usual 6 months free of charge replacement to a 12 month free of charge replacement guarantee. That is because we have so much confidence in the ability to find the right long-term candidate for your organisation using this method.</p>
        </div>
      </div>
    </section>
  </main>
</body>
</html>
```